Business Card Design Project

- makeup artist business card

- original and creative

- Elegant design

- Feel free to come out with cool designs but stick to being elegant and attractive

- Design relates to makeup

- includes name, occupation, contact numbers, email, website

- regular size business card

- round corner card

- double sided

- on 1 side it should just have the website name in the center " velvetbrushhue.com "

Industry/Entity Type

Business

Requirements
Must have
• Marla Tobin
Makeup Artist
USA: +1 (213)555-0147
Singapore: +65 90007312
marlatobin@velvetbrushhue.com
www.velvetbrushhue.com
Should not have
• nothing cartoon looking.
Pictures of makeup being grab from the internet.. Examples: eyes or lips.

```html
<!DOCTYPE html>
<html lang="en">
<head>
<meta charset="utf-8">
<title>Marla Tobin — Makeup Artist Business Card</title>
<link rel="stylesheet" href="https://fonts.googleapis.com/css2?family=Arimo:wght@400;700&display=swap">
<style>
  :root {
    --stage: #e6e4df;
    --card-black: #000000;
    --card-white: #ffffff;
    --silver: #bdbdbd;
    --mark-white: #ffffff;
    --plum: #6e2a80;
    --ink: #333333;
    --muted: #a3a3a3;
  }
  * { margin: 0; padding: 0; box-sizing: border-box; }
  html, body {
    width: 1200px;
    height: 900px;
    overflow: hidden;
    background: var(--stage);
    font-family: "Arimo", Arial, sans-serif;
  }
  .stage {
    position: relative;
    width: 1200px;
    height: 900px;
  }
  .card {
    position: absolute;
    border-radius: 28px;
    overflow: hidden;
  }
  .card-front {
    left: 52px;
    top: 56px;
    width: 693px;
    height: 447px;
    background: var(--card-black);
    z-index: 2;
  }
  .brand-line {
    position: absolute;
    left: 40px;
    top: 280px;
    display: flex;
    align-items: center;
    gap: 12px;
  }
  .brand-name {
    color: var(--silver);
    font-size: 38px;
    font-weight: 400;
    letter-spacing: 0.2px;
    line-height: 1;
  }
  .brand-mark {
    width: 96px;
    height: 96px;
    border-radius: 50%;
    background: var(--mark-white);
  }
  .card-back {
    left: 515px;
    top: 430px;
    width: 645px;
    height: 417px;
    background: var(--card-white);
    z-index: 1;
  }
  .phone-list {
    position: absolute;
    left: 28px;
    top: 392px;
    transform-origin: 0 0;
    transform: rotate(-90deg);
    color: var(--plum);
    font-size: 19px;
    line-height: 26px;
    white-space: nowrap;
  }
  .identity {
    position: absolute;
    left: 192px;
    top: 256px;
  }
  .name-row {
    display: flex;
    align-items: center;
    gap: 6px;
    margin-left: -30px;
  }
  .name-dot {
    width: 22px;
    height: 22px;
    border-radius: 50%;
    background: var(--plum);
  }
  .person-name {
    color: var(--ink);
    font-size: 21px;
    line-height: 26px;
  }
  .role {
    color: var(--muted);
    font-size: 20px;
    font-weight: 700;
    line-height: 26px;
  }
  .contact {
    margin-top: 28px;
    color: var(--ink);
    font-size: 21px;
    line-height: 28px;
  }
</style>
</head>
<body>
<main class="stage">
  <section class="card card-front" aria-label="Card front">
    <div class="brand-line">
      <span class="brand-name">www.velvetbrushhue.com</span>
      <span class="brand-mark" aria-hidden="true"></span>
    </div>
  </section>

  <section class="card card-back" aria-label="Card back">
    <div class="phone-list">
      <p>USA +1 (213)555-0147</p>
      <p>Singapore +65 90007312</p>
    </div>
    <div class="identity">
      <div class="name-row">
        <span class="name-dot" aria-hidden="true"></span>
        <h1 class="person-name">Marla Tobin</h1>
      </div>
      <p class="role">Makeup Artist</p>
      <div class="contact">
        <p>marlatobin@velvetbrushhue.com</p>
        <p>www.velvetbrushhue.com</p>
      </div>
    </div>
  </section>
</main>
</body>
</html>
```